Flyer design for our aerial photography service

We need an 8.5x11 two sided design flyer that will showcase our aerial photography service. No pricing or text is needed aside from our logo and somewhere on the page the title "Aerial Photography". I would like it be a black background with our logo in white which I have attached. Please make it a creative stylish design that highlights the photos. Our Logo should be at the top. The logo should not be large and shouldnt be the focus of the page but should be fairly visible. I'm open to it being in different locations as well.

Industry/Entity Type

Real Estate

Font styles to use
Serif

Requirements
Must have
• Logo and photos and the title Aerial Photography
Nice to have
Should not have
• n/a

```html
<!DOCTYPE html>
<html lang="en">
<head>
<meta charset="utf-8">
<title>Aerial Photography Service Flyer</title>
<link rel="stylesheet" href="https://fonts.googleapis.com/css2?family=Roboto:wght@400;500;700&family=Raleway:wght@300&family=Yellowtail&display=swap">
<style>
  :root {
    --backdrop: #2e241f;
    --sheet: #000000;
    --white: #ffffff;
    --frame: #e9e9e9;
    --band: #5a5e58;
    --band-dark: #3d403c;
    --script: #d9cdb8;
    --muted: #bdbdbd;
  }
  * { box-sizing: border-box; margin: 0; padding: 0; }
  html, body { width: 1200px; height: 857px; overflow: hidden; }
  body {
    background: var(--backdrop);
    position: relative;
    font-family: "Roboto", Arial, sans-serif;
    color: var(--white);
  }
  .flyer {
    position: absolute;
    width: 560px;
    height: 724px;
    background: var(--sheet);
    overflow: hidden;
  }
  .flyer--gallery { left: 16px; top: 70px; }
  .flyer--cover { left: 604px; top: 70px; }

  /* Gallery side */
  .photo {
    position: absolute;
    width: 220px;
    height: 138px;
    border: 2px solid var(--frame);
  }
  .col-a { left: 42px; }
  .col-b { left: 300px; }
  .row-1 { top: 27px; }
  .row-2 { top: 181px; }
  .row-3 { top: 333px; }
  .row-4 { top: 490px; }
  .tone-lake { background: linear-gradient(180deg, #a8c4de 0%, #5d7f93 30%, #5b5a4f 60%, #3f4a33 100%); }
  .tone-cottage { background: linear-gradient(180deg, #7aa4d8 0%, #5e7a4a 35%, #c2c4c4 55%, #6e9a3a 100%); }
  .tone-autumn { background: linear-gradient(160deg, #7a8fa4 0%, #9b6a3a 30%, #c67a2a 55%, #4f6a2e 100%); }
  .tone-white-house { background: linear-gradient(180deg, #dfe6ee 0%, #4d6b44 35%, #d9dcdc 55%, #3f5e2d 100%); }
  .tone-evening { background: linear-gradient(180deg, #6e8aa6 0%, #3d4f33 40%, #c7a872 55%, #3f7a2c 100%); }
  .tone-pines { background: linear-gradient(180deg, #8fa2a6 0%, #3e5a3a 40%, #9aa0a0 60%, #4a7030 100%); }
  .tone-driveway { background: linear-gradient(160deg, #c9cfd6 0%, #8a5a3a 35%, #4a4a4c 65%, #6e4a2a 100%); }
  .tone-pool { background: linear-gradient(160deg, #5e7a45 0%, #9aa0a6 35%, #3aa6c8 55%, #5f8a3a 100%); }

  .gallery-footer {
    position: absolute;
    left: 0; top: 650px;
    width: 560px; height: 74px;
  }
  .brand {
    display: flex;
    align-items: center;
    gap: 10px;
  }
  .brand-mark {
    width: 44px; height: 44px;
    border-radius: 50%;
    border: 2px solid var(--white);
    flex: none;
  }
  .brand-name {
    font-family: "Roboto", Arial, sans-serif;
    font-weight: 500;
    color: var(--white);
    letter-spacing: 1px;
    line-height: 1.15;
  }
  .gallery-footer .brand { position: absolute; left: 42px; top: 12px; }
  .gallery-footer .brand-name { font-size: 17px; }
  .divider {
    position: absolute;
    left: 303px; top: 6px;
    width: 1px; height: 58px;
    background: var(--muted);
  }
  .contact { text-align: center; }
  .gallery-footer .contact { position: absolute; left: 320px; top: 8px; width: 210px; }
  .call-label {
    font-weight: 500;
    letter-spacing: 6px;
    font-size: 14px;
  }
  .phone {
    font-weight: 700;
    font-size: 28px;
    line-height: 1.1;
    letter-spacing: 1px;
  }
  .web { font-size: 8px; letter-spacing: .5px; margin-top: 3px; }

  /* Cover side */
  .cover-scene {
    position: absolute;
    left: 0; top: 290px;
    width: 560px; height: 434px;
    background:
      radial-gradient(ellipse at 60% 60%, #3b4a52 0%, rgba(30,44,30,0) 45%),
      linear-gradient(180deg, #000 0%, #1c2a1c 20%, #22381f 55%, #2e4a24 100%);
  }
  .cover-head {
    position: absolute; left: 0; top: 24px; width: 560px;
    text-align: center;
  }
  .cover-head .brand { justify-content: center; flex-direction: column; gap: 8px; }
  .cover-head .brand-mark { width: 60px; height: 60px; }
  .cover-head .brand-name { font-size: 18px; text-transform: uppercase; letter-spacing: 2px; }
  .title-aerial {
    font-family: "Raleway", Arial, sans-serif;
    font-weight: 300;
    font-size: 28px;
    letter-spacing: 1px;
    color: #e6e6e6;
    margin-top: 16px;
  }
  .title-script {
    font-family: "Yellowtail", cursive;
    font-size: 64px;
    line-height: .9;
    color: var(--script);
    margin-top: -4px;
  }
  .service-band {
    display: inline-block;
    margin-top: 2px;
    padding: 3px 22px;
    background: linear-gradient(180deg, var(--band) 0%, var(--band-dark) 100%);
    color: #111;
    font-weight: 700;
    font-size: 20px;
    letter-spacing: 9px;
  }
  .camera-rule {
    display: block;
    margin: 8px auto 0;
  }
  .tilted {
    position: absolute;
    border: 4px solid var(--white);
  }
  .tilted--left {
    left: -4px; top: 380px; width: 212px; height: 150px;
    transform: rotate(-15deg);
    background: linear-gradient(160deg, #4a6a3a 0%, #a8a8a0 40%, #3aa6c8 70%, #8a5a3a 100%);
  }
  .tilted--right {
    left: 350px; top: 390px; width: 212px; height: 150px;
    transform: rotate(16deg);
    background: linear-gradient(160deg, #5e8a4a 0%, #3e6a2e 40%, #7a8a7a 65%, #2f5a4a 100%);
  }
  .cover-scene .contact {
    position: absolute; left: 130px; top: 330px; width: 420px;
  }
  .cover-scene .call-label { font-size: 20px; letter-spacing: 7px; }
  .cover-scene .phone { font-size: 40px; }
  .cover-scene .web { font-size: 11px; margin-top: 4px; }
</style>
</head>
<body>
  <section class="flyer flyer--gallery">
    <div class="photo col-a row-1 tone-lake" role="img" aria-label="Aerial photo of a lakeside house with hills behind"></div>
    <div class="photo col-b row-1 tone-cottage" role="img" aria-label="Aerial photo of a grey cottage with a brick path and lawn"></div>
    <div class="photo col-a row-2 tone-autumn" role="img" aria-label="High aerial photo of a neighbourhood in autumn colours"></div>
    <div class="photo col-b row-2 tone-white-house" role="img" aria-label="Aerial photo of a white house among trees"></div>
    <div class="photo col-a row-3 tone-evening" role="img" aria-label="Aerial photo of a lit house at dusk with autumn trees"></div>
    <div class="photo col-b row-3 tone-pines" role="img" aria-label="Aerial photo of a house behind tall pine trees"></div>
    <div class="photo col-a row-4 tone-driveway" role="img" aria-label="Aerial photo of a house with a wide driveway in autumn"></div>
    <div class="photo col-b row-4 tone-pool" role="img" aria-label="Aerial photo of a grey house with a pool and garden"></div>

    <footer class="gallery-footer">
      <div class="brand">
        <span class="brand-mark"></span>
        <span class="brand-name">OPEN GATE<br>PHOTOGRAPHY</span>
      </div>
      <span class="divider"></span>
      <div class="contact">
        <p class="call-label">CALL US NOW</p>
        <p class="phone">123 456 789</p>
        <p class="web">WWW.YOURWEBSITE.COM</p>
      </div>
    </footer>
  </section>

  <section class="flyer flyer--cover">
    <div class="cover-scene" role="img" aria-label="Aerial night photo of a large estate house surrounded by trees"></div>
    <div class="tilted tilted--left" role="img" aria-label="Aerial photo of a house with a deck and pool"></div>
    <div class="tilted tilted--right" role="img" aria-label="Aerial photo of a lakefront house with a dock"></div>

    <header class="cover-head">
      <div class="brand">
        <span class="brand-mark"></span>
        <span class="brand-name">Open Gate Photography</span>
      </div>
      <h1>
        <span class="title-aerial" style="display:block">AERIAL</span>
        <span class="title-script" style="display:block">Photography</span>
      </h1>
      <span class="service-band">SERVICE</span>
      <svg class="camera-rule" width="136" height="20" viewBox="0 0 136 20" aria-hidden="true">
        <g stroke="#9a9a9a" stroke-width="1.5">
          <line x1="0" y1="8" x2="44" y2="8"/><line x1="26" y1="12" x2="50" y2="12"/>
          <line x1="92" y1="8" x2="136" y2="8"/><line x1="86" y1="12" x2="110" y2="12"/>
        </g>
        <rect x="55" y="4" width="26" height="16" rx="2" fill="#cfcfcf"/>
        <rect x="62" y="1" width="10" height="4" fill="#cfcfcf"/>
        <circle cx="68" cy="12" r="5" fill="#000"/>
        <circle cx="68" cy="12" r="2.5" fill="#cfcfcf"/>
      </svg>
    </header>

    <div class="cover-scene" style="background:none">
      <div class="contact">
        <p class="call-label">CALL US NOW</p>
        <p class="phone">123 456 789</p>
        <p class="web">WWW.YOURWEBSITE.COM</p>
      </div>
    </div>
  </section>
</body>
</html>
```